Inspirational quotes poster shop seeks poster designs

Hi! We are launching an eshop with design posterss featuring inspirational quotes. We need a first poster design while looking for further cooperation on around 20 poster designs. We need outputs in the format that can go to high quality print (size at least 100x70cm).

For the first design feel free to choose any of the following quotes to depict:

1. "Stop starting. Start finishing." Author: Torvald Essunger, Klangora
2. "A problem well stated is a problem half solved." Author: Walter P. Brimsley, American inventor
3. "The best way to predict the future is to invent it." Author: Dale Hubbs, Quince

Designs should be rarther simple, think please of your whole concept and how various posters would go together. Every poster can be quite different though, in terms of fonts, colours and overall design, together they should however form and interesting collage.

Designs must contain the quote, author & company. it can be pure text or some indication of the sense of the quote.

Design must also feature company name/logo (not available yet, for now please use "thoughtvolta" as a working name), QR code with a title "Read the story"

See these posters for design we like (for inspiration ONLY!):
http://www.launchtonics.example/products/launch-print-its-simple-until-you-make-it-complicated
http://www.launchtonics.example/products/launch-print-marcus-feldane-less-meetings-more-doing
http://www.launchtonics.example/products/launch-print-gordon-ashfeld-stop-sketching-start-building

Hi to everybody! Sorry for the spam, some of you have been struggling with finding the crux in the quote, so here I offer some ideas what to look for in them. It's up to you to take it, leave it or change it:)

Stop starting, start finishing -
1 - stop starting with many times repeated small word starting, perhaps large word starting made of small words starting, with it contrasting start finishing in normal bold font.
2 - STARTING could look quite unfinished, sketchy, especially -ING could look more unfinished then the rest , e.g. just rough indication of outline of the letters, again contrasting with start finishing will clean & neat writting.

Problem well stated is a problem half solved - look for something that is clearer by defining the problem. Perhaps in a simple sketch like here http://www.launchtonics.example/products/launch-print-its-simple-until-you-make-it-complicated  point out a route from a problem (light = flame), to a solution (lightbulb, lightbulb design drawing or something like that).

Anyway, despite preference for simple design, I am still looking for some smart, creative, catchy idea in the design. Check with yourself if it's something you can would want to buy and hang up on your wall.

Good luck to all of you and again, thank you all very much for participation!
Radim

Target Market(s)

businesses of every size, from startups to large corporates seeking culture change or motivation kick up

Industry/Entity Type

Shop

Requirements
Must have
• I strongly prefer portrait orientation of the poster!

Nice to have
• Quotes themselves are often on the edge, teasing, so the design can be.
Should not have
• Try to avoid traditional dialoge bubble for the quote itself as the first obvious idea for depicting a quote.

Avoid using photos (not simple then) or too many colours.

Of course, by no means use a COPY of existing designs I linked to for inspiration. It just shows what we like.

```html
<!DOCTYPE html>
<html lang="en">
<head>
<meta charset="utf-8">
<title>Stop Starting, Start Finishing – Quote Poster</title>
<link rel="stylesheet" href="https://fonts.googleapis.com/css2?family=Montserrat:wght@400;500&family=Antonio:wght@600&family=Lobster&display=swap">
<style>
  :root {
    --backdrop: #e4e4e4;
    --paper: #ffffff;
    --blue-light: #5e9bd2;
    --blue-deep: #1f62ac;
    --ink-white: #ffffff;
  }
  html, body {
    margin: 0;
    padding: 0;
    width: 1000px;
    height: 1200px;
    overflow: hidden;
    background: var(--backdrop);
  }
  .poster-sheet {
    position: absolute;
    left: 117px;
    top: 91px;
    width: 766px;
    height: 1018px;
    background: var(--paper);
  }
  .quote-panel {
    position: absolute;
    left: 59px;
    top: 43px;
    width: 647px;
    height: 939px;
    display: block;
  }
  .outline-word {
    font-family: "Montserrat", sans-serif;
    font-weight: 400;
    fill: url(#panel-blue);
    stroke: var(--ink-white);
    stroke-width: 3.2;
    stroke-linejoin: round;
    paint-order: stroke fill;
  }
  .solid-word {
    font-family: "Antonio", sans-serif;
    font-weight: 600;
    fill: var(--ink-white);
  }
  .attribution {
    font-family: "Lobster", cursive;
    font-size: 23px;
    fill: var(--ink-white);
  }
  .attribution-rule {
    stroke: var(--ink-white);
    stroke-width: 1.2;
  }
  .shop-name {
    font-family: "Montserrat", sans-serif;
    font-weight: 500;
    font-size: 16px;
    letter-spacing: 1px;
    fill: var(--ink-white);
  }
  .qr-label {
    font-family: "Montserrat", sans-serif;
    font-weight: 500;
    font-size: 11px;
    letter-spacing: 0.5px;
    fill: var(--ink-white);
  }
  .qr-box {
    fill: none;
    stroke: var(--ink-white);
    stroke-width: 1.4;
  }
</style>
</head>
<body>
  <div class="poster-sheet">
    <svg class="quote-panel" viewBox="0 0 647 939" xmlns="http://www.w3.org/2000/svg">
      <defs>
        <linearGradient id="panel-blue" gradientUnits="userSpaceOnUse" x1="0" y1="0" x2="647" y2="939">
          <stop offset="0" stop-color="#5e9bd2"/>
          <stop offset="1" stop-color="#1f62ac"/>
        </linearGradient>
      </defs>
      <rect class="panel-fill" width="647" height="939" fill="url(#panel-blue)"/>

      <text class="outline-word headline-stop" x="97" y="257" font-size="196"
            textLength="454" lengthAdjust="spacingAndGlyphs">STOP</text>
      <text class="outline-word headline-starting" x="97" y="356" font-size="108"
            textLength="449" lengthAdjust="spacingAndGlyphs">STARTING</text>

      <text class="solid-word headline-start" x="101" y="598" font-size="262"
            textLength="447" lengthAdjust="spacingAndGlyphs">START</text>
      <text class="solid-word headline-finishing" x="101" y="769" font-size="147"
            textLength="447" lengthAdjust="spacingAndGlyphs">FINISHING</text>

      <line class="attribution-rule" x1="109" y1="813" x2="175" y2="813"/>
      <text class="attribution" x="323" y="821" text-anchor="middle">Torvald Essunger, Klangora</text>
      <line class="attribution-rule" x1="469" y1="813" x2="537" y2="813"/>

      <g class="shop-mark">
        <circle cx="115" cy="893" r="6" fill="var(--ink-white)"/>
        <text class="shop-name" x="128" y="899">thoughtvolta</text>
      </g>

      <g class="story-link">
        <text class="qr-label" x="477" y="897" text-anchor="end">Read the story</text>
        <rect class="qr-box" x="489" y="869" width="48" height="48" role="img" aria-label="QR code linking to the story behind the quote"/>
      </g>
    </svg>
  </div>
</body>
</html>
```